Vell Studio - Lash Serum Packaging

Need Packaging done for this Lash Serum for a brand called "Vell Studio". The bottle will remain black but the box can be any color. This will be for a 3ml bottle. Give me different options for packaging that is minimalist and clean for this brand that makes it look expensive and make people want to buy.

```html
<!DOCTYPE html>
<html lang="en">
<head>
<meta charset="utf-8">
<title>Vell Studio – Eyelash Growth Serum Packaging</title>
<link rel="stylesheet" href="https://fonts.googleapis.com/css2?family=Quicksand:wght@400;600;700&family=Oswald:wght@300&display=swap">
<style>
  :root {
    --page: #ffffff;
    --bottle-black: #0f0f0f;
    --cap-black: #111111;
    --copper: #b4683f;
    --copper-dark: #8d4a29;
    --muted-grey: #8a8a8a;
    --ink: #111111;
    --holo-pink: #efb8e3;
    --holo-blue: #a9def0;
    --holo-lilac: #c9b9f0;
    --holo-pearl: #f1eef3;
  }
  * { margin: 0; padding: 0; box-sizing: border-box; }
  html, body { width: 1046px; height: 1200px; overflow: hidden; background: var(--page); }
  .canvas { position: relative; width: 1046px; height: 1200px; font-family: "Quicksand", sans-serif; }

  /* Bottle */
  .bottle { position: absolute; left: 310px; top: 180px; width: 140px; height: 933px; }
  .bottle-cap {
    position: absolute; left: 0; top: 0; width: 140px; height: 355px;
    background: linear-gradient(90deg, #1c1c1c, var(--cap-black) 30%, #1a1a1a 80%, #0a0a0a);
    border-radius: 5px 5px 0 0;
  }
  .bottle-body {
    position: absolute; left: 0; top: 356px; width: 140px; height: 577px;
    background: var(--bottle-black); overflow: hidden;
  }
  .bottle-texture {
    position: absolute; inset: 0;
    background: radial-gradient(ellipse at 40% 50%, #242424 0%, var(--bottle-black) 70%);
  }
  .bottle-base { position: absolute; left: 0; bottom: 0; width: 140px; height: 14px;
    background: linear-gradient(90deg, var(--copper-dark), var(--copper), var(--copper-dark)); border-radius: 0 0 4px 4px; }
  .vertical-name {
    position: absolute; writing-mode: vertical-rl; transform: rotate(180deg);
    white-space: nowrap; font-weight: 600;
  }
  .bottle .vertical-name { left: 50px; top: 60px; font-size: 34px; color: var(--copper); letter-spacing: 2px; }
  .bottle-title {
    position: absolute; left: 0; width: 140px; top: 394px; text-align: center;
    color: var(--copper); font-weight: 700; font-size: 17px; line-height: 23px;
  }
  .bottle-tagline { position: absolute; left: 0; width: 140px; top: 484px; text-align: center;
    color: var(--muted-grey); font-size: 7px; line-height: 9px; }
  .bottle-volume { position: absolute; left: 0; width: 140px; top: 530px; text-align: center;
    color: var(--muted-grey); font-size: 6.5px; }

  /* Box */
  .box { position: absolute; left: 510px; top: 88px; width: 243px; height: 1028px; }
  .box-side, .box-front {
    position: absolute; top: 0; height: 1028px; overflow: hidden;
  }
  .box-side { left: 0; width: 51px; border-right: 1px solid rgba(0,0,0,0.06); }
  .box-front { left: 51px; width: 192px; }
  .holo {
    position: absolute; inset: 0;
    background:
      radial-gradient(ellipse at 20% 25%, var(--holo-pink) 0%, transparent 45%),
      radial-gradient(ellipse at 85% 35%, var(--holo-lilac) 0%, transparent 40%),
      radial-gradient(ellipse at 70% 70%, var(--holo-blue) 0%, transparent 45%),
      radial-gradient(ellipse at 15% 65%, var(--holo-pink) 0%, transparent 40%),
      radial-gradient(ellipse at 60% 10%, var(--holo-blue) 0%, transparent 40%),
      var(--holo-pearl);
  }
  .box-front .vertical-name { left: 62px; top: 150px; font-size: 56px; color: var(--ink); letter-spacing: 4px; font-weight: 700; }
  .box-title { position: absolute; left: 0; width: 192px; top: 718px; text-align: center;
    color: var(--ink); font-weight: 700; font-size: 26px; line-height: 33px; }
  .box-tagline { position: absolute; left: 0; width: 192px; top: 838px; text-align: center;
    color: var(--ink); font-size: 10.5px; line-height: 13px; }
  .box-volume { position: absolute; left: 0; width: 192px; top: 903px; text-align: center;
    color: var(--ink); font-weight: 700; font-size: 9.5px; }

  .badge { position: absolute; left: 8px; width: 32px; height: 110px;
    border: 1.2px solid var(--ink); border-radius: 16px; }
  .side-note { position: absolute; left: 14px; writing-mode: vertical-rl; transform: rotate(180deg);
    font-family: "Oswald", sans-serif; font-weight: 300; color: var(--ink); white-space: nowrap; }
  .side-unisex { top: 740px; font-size: 6px; left: 20px; }
  .side-claim { left: 0; width: 51px; top: 828px; writing-mode: horizontal-tb; transform: none;
    text-align: center; font-size: 10px; line-height: 16px; }
</style>
</head>
<body>
<main class="canvas">
  <section class="bottle" aria-label="Bottle label">
    <div class="bottle-cap"></div>
    <div class="bottle-body">
      <div class="bottle-texture" role="img" aria-label="Fine flowing line pattern on black"></div>
      <span class="vertical-name">Vell Studio</span>
      <h2 class="bottle-title">EYELASH<br>GROWTH<br>SERUM</h2>
      <p class="bottle-tagline">Strengthens and enhances<br>your lashes in 30 Days</p>
      <p class="bottle-volume">3ML | 0.1 FL.OZ.</p>
      <div class="bottle-base"></div>
    </div>
  </section>

  <section class="box" aria-label="Box dieline">
    <div class="box-side">
      <div class="holo" role="img" aria-label="Holographic pastel swirl"></div>
      <div class="badge" style="top:97px"></div>
      <div class="badge" style="top:260px"></div>
      <div class="badge" style="top:427px"></div>
      <div class="badge" style="top:593px"></div>
      <span class="side-note side-unisex">Unisex | Unisexe | Unisexo</span>
      <p class="side-note side-claim">REDEFINING<br>NATURAL<br>LASH<br>GROWTH</p>
    </div>
    <div class="box-front">
      <div class="holo" role="img" aria-label="Holographic pastel swirl"></div>
      <span class="vertical-name">Vell Studio</span>
      <h1 class="box-title">EYELASH<br>GROWTH<br>SERUM</h1>
      <p class="box-tagline">Strengthens and enhances<br>your lashes in 30 Days</p>
      <p class="box-volume">3ML | 0.1 FL.OZ.</p>
    </div>
  </section>
</main>
</body>
</html>
```